Mobile Recording Studio needs business cards

Open to seeing a creative design, but I want to emphasis my logo and minimize the name/title and company information. Possible a fully black background on card.

My company is a mobile sound recording studio. ok to include a my trailer (actual or cartoon) on the card. My initial thought is more straight forward, but a good design will win me over.

SPECS:
CMYK color mode
High (300ppi) raster effect.
cover bleed area
please deliver: Illustrator file with layers and a pdf at completion.

Name and info for the business card:

Dallin Perry
ADR Mixer

email: Dallin@MixVault.com

address:
248 - 5170 East Hollister
Vancouver, BC V5R 2J4

phone:
604.518.2093 office

website:
www.MixVault.com

FB: @MixVault

Instagram: @TheMixVault

Industry/Entity Type

Television Production

Contact Information for Business Card

Dallin Perry
ADR Mixer

email: Dallin@MixVault.com

address:
248 - 5170 East Hollister
Vancouver, BC V5R 2J4

phone:
604.518.2093 office

website:
www.MixVault.com

FB: @MixVault

Instagram: @TheMixVault

Colors

Designer to choose colors to be used in the design.

Requirements
Must have
• emphasis my logo and minimize the name/title and company information.
• SPECS:
• CMYK color mode
• High (300ppi) raster effect.
• cover bleed area
• please deliver: Illustrator file with layers and a pdf at completion.
Nice to have
• maybe include the following:
• all black background or black theme
• my work trailer (actual or cartoon) refer to Instagram: @TheMixVault

```html
<!DOCTYPE html>
<html lang="en">
<head>
<meta charset="utf-8">
<title>MixVault — Business Cards</title>
<link href="https://fonts.googleapis.com/css2?family=Arimo:wght@400;700&display=swap" rel="stylesheet">
<style>
  :root {
    --backdrop: #d4d4d4;
    --card-black: #121212;
    --card-dark: #2a2a2a;
    --card-mid: #4a4a4a;
    --silver: #d9d9d9;
    --text-light: #f2f2f2;
    --text-soft: #bdbdbd;
    --strip: #1c1c1c;
  }
  * { box-sizing: border-box; margin: 0; padding: 0; }
  html, body { width: 1200px; height: 913px; overflow: hidden; }
  body {
    background: var(--backdrop);
    font-family: "Arimo", Arial, sans-serif;
    display: flex;
    align-items: center;
    justify-content: center;
    gap: 60px;
  }
  .card {
    width: 520px;
    height: 297px;
    border-radius: 4px;
    overflow: hidden;
    position: relative;
    box-shadow: 0 12px 30px rgba(0,0,0,0.28);
  }

  /* Back: contact side */
  .card-back { background: var(--card-black); display: flex; flex-direction: column; }
  .trailer-photo {
    height: 136px;
    background: linear-gradient(180deg, #e4e4e4 0%, #a9a9a9 45%, #3d3d3d 100%);
    position: relative;
  }
  .social-strip {
    position: absolute;
    left: 0; bottom: 0;
    width: 210px;
    background: var(--strip);
    padding: 8px 12px;
    display: flex;
    flex-direction: column;
    gap: 6px;
  }
  .social-item { display: flex; align-items: center; gap: 8px; color: var(--text-light); font-size: 13px; }
  .social-mark { width: 13px; height: 13px; background: var(--text-light); border-radius: 2px; }
  .contact { padding: 18px 24px; color: var(--text-light); line-height: 1.35; }
  .person-name { font-weight: 700; font-size: 15px; }
  .person-role { font-size: 12px; color: var(--text-soft); margin-bottom: 4px; }
  .address { font-size: 12px; margin-top: 6px; color: var(--text-light); }

  /* Front: logo side */
  .card-front {
    background: radial-gradient(ellipse at 45% 45%, var(--card-mid) 0%, var(--card-dark) 40%, var(--card-black) 85%);
    display: flex;
    align-items: center;
    justify-content: center;
  }
  .brand-name {
    font-weight: 700;
    font-size: 78px;
    color: var(--silver);
    letter-spacing: 1px;
  }
</style>
</head>
<body>
  <section class="card card-back">
    <div class="trailer-photo" role="img" aria-label="Black and white photo of the mobile recording trailer parked among snowy trees">
      <div class="social-strip">
        <div class="social-item"><span class="social-mark"></span>@MixVault</div>
        <div class="social-item"><span class="social-mark"></span>@TheMixVault</div>
      </div>
    </div>
    <div class="contact">
      <p class="person-name">Dallin Perry</p>
      <p class="person-role">ADR mixer</p>
      <p class="person-name">Reid Calloway</p>
      <p class="person-role">Engineer / Director of Operations</p>
      <p class="address">248 - 5170 East Hollister<br>
        Vancouver | BC V5R 2J4<br>
        604.518.2093 | www.MixVault.com</p>
    </div>
  </section>

  <section class="card card-front">
    <h1 class="brand-name">MixVault</h1>
  </section>
</body>
</html>
```